Wordpress theme customised please - for new ecommerce homewares website

Hi, we need a wordpress theme customised for a business that will sell tea towels (aka kitchen towels/dish cloths).
We do not have a website currently, but wish to launch using wordpress + woocommerce + "the shopfront" theme (c/- plumkestrel).
BACKGROUND RE THE BUSINESS
Our products are very stylish and will appeal to people who like owning gorgeous things - people who love cooking and/or decorating their home beautifully, or maybe they like travelling and/or buying presents for themselves and friends/family etc.
As they are typically used in people's kitchens, so "fresh" and "clean" is important - however the site must look very upmarket: timeless yet current, and classic yet simple, but not pretty, fussy or edgy.
We believe we have a great opportunity to leverage the "feel" of the product - cotton & linen fabric that has real texture to it, is tactile, natural, raw, real... in the photos used on the website, the backgrounds etc
Our logo is attached - a very dark grey colour was chosen, with white stripes, so that its neutral colouring would coordinate well with our suppliers' existing packaging. (We will represent a number of brands.)
BACKGROUND RE THIS PROJECT
We already know we want to use "the shopfront" theme by plumkestrel, but we need help customising the look of this theme so it works well with our logo, looks really striking and doesn't look like everyone else's ie "straight out of the box".
It appears these are the types of things that can be changed:
LAYOUT:
home page design concept (eg with a cascade carousel)
page design concept for eg About Us, Contact Us, FAQs
landing page design concept
header; light footer; dark footer
COLOURS & BACKGROUNDS & BORDERS & SEPARATORS:
main theme colour; accent colour; primary font colour
header background; light footer background colour; dark footer background colour; copyright bar background colour
dark footer widget title border; dark footer list separators and borders; dark footer/copyright bar separator styles
FONTS:
main navigation text colour; secondary navigation text colour; dark footer text colour; copyright bar text colour
main font; secondary font
LASTLY
Please don't hesitate to ask questions, request further information etc This is the first time we've posted a design project like this so it's tricky to know what other information you will need, so please just get in touch, ok!
Thanks so much for your interest in this project, and best wishes.

```html
<!DOCTYPE html>
<html lang="en">
<head>
<meta charset="utf-8">
<title>Dishcloth Row – Home</title>
<link href="https://fonts.googleapis.com/css2?family=Lato:wght@400;700&family=Libre+Baskerville:wght@400&family=Roboto+Condensed:wght@700&family=Oswald:wght@500&display=swap" rel="stylesheet">
<style>
:root{
  --topbar:#141414;
  --header:#262b37;
  --accent:#fcc713;
  --ink:#1e1e1e;
  --muted:#7a7a7a;
  --price:#e2231a;
  --card:#f1f1f1;
  --card-line:#dddddd;
  --white:#ffffff;
}
*{margin:0;padding:0;box-sizing:border-box}
html,body{width:1121px;height:1200px;overflow:hidden;background:var(--white);font-family:'Lato',sans-serif;color:var(--ink)}
.page{position:relative;width:1121px;height:1200px}
.abs{position:absolute}

.topbar{left:33px;top:0;width:1056px;height:41px;background:var(--topbar)}
.social{left:18px;top:12px;display:flex;gap:12px}
.social span{display:block;width:14px;height:14px;border-radius:50%;background:var(--white)}
.account-links{right:64px;top:0;height:41px;display:flex;align-items:center;gap:9px;color:var(--white);font-size:11px;font-weight:700}
.search{right:10px;top:0;width:46px;height:41px;border-left:1px solid #2c2c2c;display:flex;align-items:center;justify-content:center}

.header{left:33px;top:41px;width:1056px;height:128px;background:var(--header)}
.brand{left:13px;top:56px;color:var(--white);font-family:'Libre Baskerville',serif;font-size:34px;letter-spacing:1px;line-height:1}
.cart{left:919px;top:21px;display:flex;align-items:center}
.cart-count{border:2px solid var(--accent);color:var(--accent);font-size:10px;font-weight:700;padding:2px 10px;height:21px;line-height:15px}
.nav{right:15px;top:72px;display:flex;gap:16px;color:var(--white);font-size:14px}
.nav .sep{opacity:.9}

.hero{left:33px;top:169px;width:1056px;height:463px;background:radial-gradient(ellipse at 55% 45%,#f1f1ee 0%,#d9d5cc 28%,#c9ad6f 45%,#3a3a34 70%,#25251f 100%)}
.hero-arrow{width:28px;height:28px;background:#000;display:flex;align-items:center;justify-content:center}
.dots{left:512px;top:600px;width:100px;height:32px;background:#1c1c1c;border-radius:6px 6px 0 0;display:flex;align-items:center;justify-content:center;gap:6px}
.dots span{width:13px;height:13px;border-radius:50%;background:#555}
.dots span.on{background:var(--accent)}

.shipping{left:0;top:660px;width:1121px;height:106px;background:linear-gradient(#ececec,#fff 14%,#fff 86%,#ececec)}
.shipping-text{left:0;width:975px;top:36px;text-align:center;font-family:'Roboto Condensed',sans-serif;font-weight:700;font-size:29px;color:var(--ink)}
.badge{left:838px;top:647px;width:130px;height:130px;border-radius:50%;background:var(--white);box-shadow:0 3px 8px rgba(0,0,0,.35);display:flex;align-items:center;justify-content:center}
.badge-inner{width:108px;height:108px;border-radius:50%;background:var(--accent);display:flex;align-items:center;justify-content:center;text-align:center;font-size:14px;line-height:1.3;padding:0 10px}

.section-title{left:45px;top:797px;font-family:'Oswald',sans-serif;font-weight:500;font-size:27px;color:var(--ink)}
.section-nav{top:812px;width:28px;height:28px;background:#000;display:flex;align-items:center;justify-content:center}
.rule-dark{left:45px;top:841px;width:203px;height:7px;background:#3a3a3a}
.rule-accent{left:248px;top:841px;width:829px;height:7px;background:var(--accent)}

.card{top:866px;width:243px;height:275px;background:var(--card);border:1px solid var(--card-line)}
.card-title{position:absolute;left:0;width:100%;top:17px;text-align:center;font-size:20px}
.card-photo{position:absolute;left:21px;top:50px;width:200px;height:160px}
.card-model{position:absolute;left:34px;top:227px;font-size:11px;color:var(--muted)}
.card-price{position:absolute;left:34px;top:242px;font-size:11px;color:var(--price);font-weight:700}
.buy{position:absolute;left:141px;top:225px;width:74px;height:25px;background:var(--ink);color:var(--white);font-size:11px;font-weight:700;display:flex;align-items:center;justify-content:center;border-radius:2px}
</style>
</head>
<body>
<div class="page">

  <div class="abs topbar">
    <div class="abs social" aria-label="Social links">
      <span></span><span></span><span></span><span></span><span></span><span></span><span></span><span></span>
    </div>
    <div class="abs account-links">
      <span>TRACK YOUR ORDER</span><span>|</span><span>MY ACCOUNT</span><span>|</span><span>REGISTER</span>
    </div>
    <div class="abs search">
      <svg width="18" height="18" viewBox="0 0 18 18"><circle cx="7.5" cy="7.5" r="5.5" fill="none" stroke="#8a8a8a" stroke-width="2.4"/><line x1="11.5" y1="11.5" x2="16.5" y2="16.5" stroke="#8a8a8a" stroke-width="2.8" stroke-linecap="round"/></svg>
    </div>
  </div>

  <header class="abs header">
    <div class="abs brand">DISHCLOTH ROW</div>
    <div class="abs cart">
      <span class="cart-count">0 ITEMS</span>
      <svg width="26" height="26" viewBox="0 0 26 26" style="margin-left:-6px;margin-top:-8px"><g transform="rotate(-15 13 13)"><rect x="4" y="8" width="18" height="15" rx="2" fill="#fcc713"/><path d="M9 9 V6 a4 4 0 0 1 8 0 V9" fill="none" stroke="#fcc713" stroke-width="2"/></g></svg>
    </div>
    <nav class="abs nav">
      <span>HOME</span><span class="sep">|</span><span>ABOUT</span><span class="sep">|</span><span>SERVICES</span><span class="sep">|</span><span>PRODUCTS</span><span class="sep">|</span><span>BLOG</span><span class="sep">|</span><span>CONTACT</span>
    </nav>
  </header>

  <div class="abs hero" role="img" aria-label="Carousel slide: white herringbone tea towel with a blue stripe draped over a cream ceramic dish on a dark cloth"></div>
  <div class="abs hero-arrow" style="left:42px;top:387px"><svg width="10" height="12" viewBox="0 0 10 12"><path d="M8 1 L2 6 L8 11" fill="none" stroke="#fff" stroke-width="2.5"/></svg></div>
  <div class="abs hero-arrow" style="left:1051px;top:387px"><svg width="10" height="12" viewBox="0 0 10 12"><path d="M2 1 L8 6 L2 11" fill="none" stroke="#fff" stroke-width="2.5"/></svg></div>
  <div class="abs dots"><span class="on"></span><span></span><span></span><span></span><span></span></div>

  <div class="abs shipping">
    <div class="abs shipping-text">FREE SHIPPING ON ALL ORDERS OVER $50.00</div>
  </div>
  <div class="abs badge"><div class="badge-inner">Deliver to your doors on 3 days</div></div>

  <h2 class="abs section-title">FEATURED PRODUCTS</h2>
  <div class="abs section-nav" style="left:1019px"><svg width="10" height="12" viewBox="0 0 10 12"><path d="M8 1 L2 6 L8 11" fill="none" stroke="#fff" stroke-width="2.5"/></svg></div>
  <div class="abs section-nav" style="left:1050px"><svg width="10" height="12" viewBox="0 0 10 12"><path d="M2 1 L8 6 L2 11" fill="none" stroke="#fff" stroke-width="2.5"/></svg></div>
  <div class="abs rule-dark"></div>
  <div class="abs rule-accent"></div>

  <article class="abs card" style="left:45px">
    <div class="card-title">Boys Shoes</div>
    <div class="card-photo" role="img" aria-label="Hanging tea towel with a blue lattice fabric top and brown terry towel" style="background:linear-gradient(#8fd0e0 0%,#6fb6c8 55%,#7b6a5f 75%,#6a5b52 100%)"></div>
    <div class="card-model">MODEL 12458</div>
    <div class="card-price">$25.69</div>
    <div class="buy">BUY NOW</div>
  </article>

  <article class="abs card" style="left:308px">
    <div class="card-title">Girls Clothes</div>
    <div class="card-photo" role="img" aria-label="White towel gathered with a green ruffled fabric band" style="background:linear-gradient(90deg,#3a2418 0%,#e9e6df 30%,#b9d08a 50%,#e9e6df 70%,#3a2418 100%)"></div>
    <div class="card-model">MODEL 12458</div>
    <div class="card-price">$25.69</div>
    <div class="buy">BUY NOW</div>
  </article>

  <article class="abs card" style="left:571px">
    <div class="card-title">Girls Shoes</div>
    <div class="card-photo" role="img" aria-label="Row of printed tea towels in black, linen and cream" style="background:linear-gradient(90deg,#222 0%,#333 30%,#c9b8a8 50%,#ddd3c6 75%,#c8bba9 100%)"></div>
    <div class="card-model">MODEL 12458</div>
    <div class="card-price">$25.69</div>
    <div class="buy">BUY NOW</div>
  </article>

  <article class="abs card" style="left:834px">
    <div class="card-title">Norsey Decors</div>
    <div class="card-photo" role="img" aria-label="Linen tea towel with a teal seahorse print" style="background:radial-gradient(circle at 50% 50%,#5fb3b3 0%,#a7c9c3 35%,#e2ddd6 65%)"></div>
    <div class="card-model">MODEL 12458</div>
    <div class="card-price">$25.69</div>
    <div class="buy">BUY NOW</div>
  </article>

</div>
</body>
</html>
```